Banner Ads for Online Poker Promotion

We are an online poker network, the KVR (www.thekvr.eu). We are looking for a small selection of web banner ads for our latest promotion and we are trying crowdsourcing for the first time!

Banner sizes that we need are:
- 196x523 (static .psd and .png)
- 199x129 (static .psd and .png)
- 447x426 (static .psd and .png)
- 500x400 (static .psd and .png)
- 697x167 (static .psd and .png)
- 460x60 (animated .gif)

The promotion name is ‘Lucky Lap’ and the concept is that a person who enters one of the specified tournaments four or more times during the promotion will win a free ticket to play that tournament again. So effectively a ‘Loop Twice, Gain Extra Spin’ promo. We also are giving away €10,000 in free entries to the tournaments during the promotion. The specific tournaments are called ‘Quiet Dusk Up’ and ‘The Zeal Den’ and run daily on our network. The promotion runs October 1 – 31.

Guidelines:

The name of the promotion, ‘Lucky Lap’, should feature prominently in the banners.

The strap line can be ‘Loop Twice, Gain Extra Spin’ or something that encourages players to ‘take a shot’ at the tournaments.

Our network logo may feature, but is not absolutely necessary.

Examples of past promotional imagery can be found on our website, in particular these pages: http://www.thekvr.eu/promotions/ and http://www.thekvr.eu/promotions/archived-promotions/

We are looking to go in a more modern and risqué direction than the past, in order to stand out from competition which is very bland.

Please do not use common poker imagery – so no cards, chips, suit icons etc – or objects associated with live poker (tables, etc). This sort of imagery is too clichéd.

More like iOS7, less like iOS6

Think glamour, neon, rock music, extreme sports, and the Gilt Ledge!

If any further guidance is needed please don’t hesitate to ask.

```html
<!DOCTYPE html>
<html lang="en">
<head>
<meta charset="utf-8">
<title>Lucky Lap — Banner Set</title>
<link rel="stylesheet" href="https://fonts.googleapis.com/css2?family=Lato:wght@400;700;900&family=Teko:wght@500;600&display=swap">
<style>
  :root {
    --page-bg: #e4e4e6;
    --page-glow: #f2f2f3;
    --banner-dark: #1f1f21;
    --banner-mid: #4a4a4d;
    --banner-light: #707074;
    --text-white: #ffffff;
    --text-soft: #e6e6e8;
    --chrome-top: #ffffff;
    --chrome-mid: #c9c9cd;
    --chrome-low: #7d7d82;
    --chrome-bottom: #f4f4f6;
    --gem-red: #c0162c;
  }
  * { box-sizing: border-box; margin: 0; padding: 0; }
  html, body { width: 1200px; height: 857px; overflow: hidden; }
  body {
    position: relative;
    background: radial-gradient(ellipse at 50% 45%, var(--page-glow) 0%, var(--page-bg) 70%);
    font-family: "Lato", Arial, sans-serif;
    color: var(--text-white);
  }
  .banner {
    position: absolute;
    overflow: hidden;
    background: var(--banner-dark);
    box-shadow: 0 1px 3px rgba(0,0,0,.25);
  }
  .banner-backdrop {
    position: absolute; inset: 0;
    background:
      radial-gradient(circle at 50% 50%, rgba(192,22,44,.18) 0%, rgba(192,22,44,0) 30%),
      radial-gradient(ellipse at 50% 50%, var(--banner-light) 0%, var(--banner-mid) 35%, var(--banner-dark) 100%);
  }
  .banner > *:not(.banner-backdrop) { position: absolute; }
  .prize {
    display: flex; align-items: baseline; gap: 14px;
    white-space: nowrap;
  }
  .prize-amount {
    font-weight: 900;
    letter-spacing: -0.5px;
    background: linear-gradient(180deg, var(--chrome-top) 0%, var(--chrome-mid) 55%, var(--chrome-low) 70%, var(--chrome-bottom) 100%);
    -webkit-background-clip: text; background-clip: text;
    -webkit-text-fill-color: transparent;
    filter: drop-shadow(0 2px 2px rgba(0,0,0,.6));
  }
  .prize-label { font-weight: 400; color: var(--text-soft); letter-spacing: .3px; }
  .promo-title {
    font-family: "Teko", "Arial Narrow", sans-serif;
    font-weight: 600;
    line-height: .8;
    white-space: nowrap;
    text-align: center;
    background: linear-gradient(180deg, var(--chrome-top) 0%, var(--chrome-mid) 48%, var(--chrome-low) 58%, var(--chrome-top) 78%, var(--chrome-bottom) 100%);
    -webkit-background-clip: text; background-clip: text;
    -webkit-text-fill-color: transparent;
    filter: drop-shadow(0 3px 3px rgba(0,0,0,.7));
  }
  .tagline {
    white-space: nowrap; text-align: center;
    font-weight: 400; letter-spacing: .6px;
    text-shadow: 0 1px 3px rgba(0,0,0,.8);
  }
  .tagline strong { font-weight: 900; }
  .dates {
    white-space: nowrap; text-align: center;
    font-weight: 400; letter-spacing: .3px;
    text-shadow: 0 1px 2px rgba(0,0,0,.8);
  }
  .network-name {
    display: flex; align-items: center; gap: 6px;
    font-weight: 400; font-size: 17px; letter-spacing: .5px; color: var(--text-white);
  }
  .network-name .mark { width: 8px; height: 8px; background: var(--text-white); }
  .centered { left: 0; right: 0; text-align: center; justify-content: center; }

  /* 697 × 167 leaderboard */
  .banner--wide { left: 107px; top: 72px; width: 697px; height: 167px; }
  .banner--wide .prize { left: 15px; top: 10px; flex-direction: column; align-items: center; gap: 2px; }
  .banner--wide .prize-amount { font-size: 34px; }
  .banner--wide .prize-label { font-size: 12px; }
  .banner--wide .network-name { left: 18px; top: 131px; }
  .banner--wide .dates { right: 18px; top: 17px; font-size: 14px; }
  .banner--wide .promo-title { left: 150px; width: 360px; top: 34px; font-size: 96px; }
  .banner--wide .tagline { left: 150px; width: 360px; top: 130px; font-size: 16px; }

  /* 199 × 129 small */
  .banner--small { left: 825px; top: 106px; width: 199px; height: 129px; }
  .banner--small .prize { top: 7px; gap: 5px; }
  .banner--small .prize-amount { font-size: 20px; }
  .banner--small .prize-label { font-size: 11px; }
  .banner--small .promo-title { top: 36px; font-size: 50px; }
  .banner--small .tagline { top: 87px; font-size: 10px; letter-spacing: 0; font-weight: 700; }
  .banner--small .dates { top: 105px; font-size: 12px; }

  /* 500 × 400 */
  .banner--landscape { left: 18px; top: 261px; width: 500px; height: 399px; }
  .banner--landscape .prize { top: 22px; }
  .banner--landscape .prize-amount { font-size: 34px; }
  .banner--landscape .prize-label { font-size: 13px; }
  .banner--landscape .promo-title { top: 106px; font-size: 126px; }
  .banner--landscape .tagline { top: 237px; font-size: 19px; }
  .banner--landscape .dates { top: 357px; font-size: 15px; }

  /* 196 × 523 skyscraper */
  .banner--tall { left: 530px; top: 259px; width: 196px; height: 536px; }
  .banner--tall .prize { top: 18px; flex-direction: column; align-items: center; gap: 4px; }
  .banner--tall .prize-amount { font-size: 34px; }
  .banner--tall .prize-label { font-size: 13px; font-weight: 700; }
  .banner--tall .promo-title { top: 158px; font-size: 82px; line-height: 1; }
  .banner--tall .tagline { top: 336px; font-size: 20px; line-height: 1.15; }
  .banner--tall .dates { top: 495px; font-size: 15px; }

  /* 447 × 426 */
  .banner--square { left: 734px; top: 261px; width: 447px; height: 425px; }
  .banner--square .prize { top: 25px; }
  .banner--square .prize-amount { font-size: 34px; }
  .banner--square .prize-label { font-size: 14px; }
  .banner--square .promo-title { top: 130px; font-size: 116px; }
  .banner--square .tagline { top: 252px; font-size: 18px; }
  .banner--square .dates { top: 380px; font-size: 15px; }

  /* 460 × 60 strip */
  .banner--strip { left: 34px; top: 686px; width: 468px; height: 60px; }
  .banner--strip .promo-title { left: 10px; top: 13px; font-size: 46px; text-align: left; }
  .banner--strip .tagline { left: 189px; top: 21px; font-size: 17px; text-align: left; }
</style>
</head>
<body>

<section class="banner banner--wide" aria-label="Leaderboard banner">
  <div class="banner-backdrop" role="img" aria-label="Dark radiating light burst with scattered red and white gems"></div>
  <div class="prize"><span class="prize-amount">€10,000</span><span class="prize-label">IN FREE ENTRIES</span></div>
  <div class="network-name"><span class="mark"></span>KVR</div>
  <h1 class="promo-title">Lucky Lap</h1>
  <p class="tagline">LOOP TWICE, GAIN EXTRA <strong>SPIN</strong></p>
  <p class="dates">OCTOBER 1 – 31</p>
</section>

<section class="banner banner--small" aria-label="Small banner">
  <div class="banner-backdrop" role="img" aria-label="Dark radiating light burst with scattered gems"></div>
  <div class="prize centered"><span class="prize-amount">€10,000</span><span class="prize-label">IN FREE ENTRIES</span></div>
  <h1 class="promo-title centered">Lucky Lap</h1>
  <p class="tagline centered">LOOP TWICE, GAIN EXTRA SPIN</p>
  <p class="dates centered">OCTOBER 1 – 31</p>
</section>

<section class="banner banner--landscape" aria-label="Landscape banner">
  <div class="banner-backdrop" role="img" aria-label="Dark radiating light burst with scattered red and white gems"></div>
  <div class="prize centered"><span class="prize-amount">€10,000</span><span class="prize-label">IN FREE ENTRIES</span></div>
  <h1 class="promo-title centered">Lucky Lap</h1>
  <p class="tagline centered">LOOP TWICE, GAIN EXTRA <strong>SPIN</strong></p>
  <p class="dates centered">OCTOBER 1 – 31</p>
</section>

<section class="banner banner--tall" aria-label="Skyscraper banner">
  <div class="banner-backdrop" role="img" aria-label="Dark radiating light burst with scattered red and white gems"></div>
  <div class="prize centered"><span class="prize-amount">€10,000</span><span class="prize-label">IN FREE ENTRIES</span></div>
  <h1 class="promo-title centered">Lucky<br>Lap</h1>
  <p class="tagline centered">LOOP TWICE<br>GAIN EXTRA <strong>SPIN</strong></p>
  <p class="dates centered">OCTOBER 1 – 31</p>
</section>

<section class="banner banner--square" aria-label="Square banner">
  <div class="banner-backdrop" role="img" aria-label="Dark radiating light burst with scattered red and white gems"></div>
  <div class="prize centered"><span class="prize-amount">€10,000</span><span class="prize-label">IN FREE ENTRIES</span></div>
  <h1 class="promo-title centered">Lucky Lap</h1>
  <p class="tagline centered">LOOP TWICE, GAIN EXTRA <strong>SPIN</strong></p>
  <p class="dates centered">OCTOBER 1 – 31</p>
</section>

<section class="banner banner--strip" aria-label="Strip banner">
  <div class="banner-backdrop" role="img" aria-label="Dark radiating light burst with red gems"></div>
  <h1 class="promo-title">Lucky Lap</h1>
  <p class="tagline">LOOP TWICE, GAIN EXTRA <strong>SPIN</strong></p>
</section>

</body>
</html>
```